New Business Card Needed

I need a new business card for Willowmere Kitchen & Bath.
Logo is attached as well a my photo. Note: Make the logo Navy Blue.
Here is the text:
Desmond Ferrick
GC/Owner
Larkfield OR
555-555-0183
desmond@willowmereKB.example
www.willowmereKB.example
Tag line on card: BEAUTY | FUNCTION | ON TIME | ON BUDGET
Trim size: 2.56" X 2.56"
This is where we aim to cut the cards.
Safe area: 2.4" X 2.4"
Make sure any important aspects of your design such as text and logos are inside of the safe area, otherwise they may be cut off.
Bleed area: 2.71 X 2.71
Make sure that your background extends to fill the bleed to avoid your Business Cards having white edges when trimmed.
On the back side. Use photo of kitchen attached.

```html
<!DOCTYPE html>
<html lang="en">
<head>
<meta charset="utf-8">
<title>Willowmere Kitchen &amp; Bath – Business Card</title>
<link href="https://fonts.googleapis.com/css2?family=Raleway:wght@700&family=Roboto:wght@400;500&family=Montserrat:wght@400&display=swap" rel="stylesheet">
<style>
  :root {
    --stage: #d2d3d5;
    --navy: #0b1540;
    --white: #ffffff;
    --grey-text: #6b6b6f;
    --portrait-tone: #4a4a4e;
  }
  * { margin: 0; padding: 0; box-sizing: border-box; }
  html, body { width: 1200px; height: 1000px; overflow: hidden; }
  body { background: var(--stage); position: relative; }

  .card { position: absolute; top: 268px; width: 462px; height: 463px; overflow: hidden; }

  /* Front */
  .card-front { left: 128px; background: var(--white); }
  .front-band { position: absolute; left: 0; top: 0; width: 100%; height: 123px; background: var(--navy); }
  .portrait {
    position: absolute; left: 50px; top: 46px; width: 156px; height: 156px;
    border-radius: 50%; border: 5px solid var(--white);
    background: radial-gradient(circle at 50% 40%, #8a7466 0%, #5a4e48 45%, var(--portrait-tone) 100%);
  }
  .person-name {
    position: absolute; left: 50px; top: 235px;
    font: 700 28px/1 "Raleway", sans-serif; color: var(--navy);
  }
  .person-role {
    position: absolute; left: 50px; top: 270px;
    font: 400 21px/1 "Roboto", sans-serif; color: var(--grey-text);
  }
  .contact-list { position: absolute; left: 49px; top: 306px; list-style: none; }
  .contact-item {
    display: flex; align-items: center; gap: 6px; height: 28.7px;
    font: 400 19.5px/1 "Montserrat", sans-serif; color: var(--grey-text);
  }
  .contact-icon { width: 19px; height: 19px; flex: none; fill: var(--navy); }
  .contact-icon-outline { fill: none; stroke: var(--navy); stroke-width: 1.8; }

  /* Back */
  .card-back { left: 610px; }
  .kitchen-photo {
    position: absolute; inset: 0;
    background:
      linear-gradient(180deg, rgba(28,36,80,0.95) 0%, rgba(40,46,92,0.75) 55%, rgba(70,62,100,0.7) 100%),
      linear-gradient(90deg, #3a3c5e 0%, #9a9ab0 55%, #8a7a6a 100%);
  }
  .brand {
    position: absolute; left: 50px; top: 52px; display: flex; align-items: center; gap: 14px;
  }
  .brand-square { width: 22px; height: 22px; border: 3px solid var(--white); flex: none; }
  .brand-name {
    font: 500 38px/1.1 "Roboto", sans-serif; color: var(--white); letter-spacing: 0.5px;
  }
  .tagline {
    position: absolute; left: 49px; top: 394px; display: flex; gap: 8px;
    font: 500 14.5px/1 "Roboto", sans-serif; color: var(--white); white-space: nowrap;
  }
  .tagline-item { display: flex; align-items: center; gap: 6px; }
  .tagline-item::before {
    content: ""; width: 9px; height: 9px; border: 1.3px solid var(--white);
  }
</style>
</head>
<body>
  <section class="card card-front">
    <div class="front-band"></div>
    <div class="portrait" role="img" aria-label="Portrait photo of Desmond Ferrick"></div>
    <h1 class="person-name">Desmond Ferrick</h1>
    <p class="person-role">GC/Owner</p>
    <ul class="contact-list">
      <li class="contact-item">
        <svg class="contact-icon" viewBox="0 0 24 24"><path d="M6.6 10.8a15.2 15.2 0 0 0 6.6 6.6l2.2-2.2a1 1 0 0 1 1-.25 11.4 11.4 0 0 0 3.6.57 1 1 0 0 1 1 1V20a1 1 0 0 1-1 1A17 17 0 0 1 3 4a1 1 0 0 1 1-1h3.5a1 1 0 0 1 1 1c0 1.25.2 2.45.57 3.57a1 1 0 0 1-.25 1z"/></svg>
        555-555-0183
      </li>
      <li class="contact-item">
        <svg class="contact-icon" viewBox="0 0 24 24"><path d="M2 5h20v14H2z M4 7v.3l8 5.4 8-5.4V7z M4 9.7V17h16V9.7l-8 5.4z" fill-rule="evenodd"/></svg>
        desmond@willowmereKB.example
      </li>
      <li class="contact-item">
        <svg class="contact-icon contact-icon-outline" viewBox="0 0 24 24"><circle cx="12" cy="12" r="9"/><ellipse cx="12" cy="12" rx="4" ry="9"/><path d="M3 12h18M4.5 7.5h15M4.5 16.5h15"/></svg>
        www.willowmereKB.example
      </li>
      <li class="contact-item">
        <svg class="contact-icon" viewBox="0 0 24 24"><path d="M12 1.5a7.5 7.5 0 0 0-7.5 7.5c0 5.6 7.5 13.5 7.5 13.5s7.5-7.9 7.5-13.5A7.5 7.5 0 0 0 12 1.5zm0 10.5a3 3 0 1 1 0-6 3 3 0 0 1 0 6z"/></svg>
        Larkfield OR
      </li>
    </ul>
  </section>

  <section class="card card-back">
    <div class="kitchen-photo" role="img" aria-label="Photo of a bright kitchen with white island and wood cabinets, under a navy tint"></div>
    <div class="brand">
      <span class="brand-square"></span>
      <p class="brand-name">Willowmere<br>Kitchen &amp; Bath</p>
    </div>
    <p class="tagline">
      <span class="tagline-item">BEAUTY</span>
      <span class="tagline-item">FUNCTION</span>
      <span class="tagline-item">ON TIME</span>
      <span class="tagline-item">ON BUDGET</span>
    </p>
  </section>
</body>
</html>
```